Waterjet Cutting Business requires an up to date website

We currently have a website which is outdated and in need of modernization.
We are only looking for a simple website with around 4 pages: Home, Contact Us, Materials, Gallery.
We have some pictures and a logo which can be used.
Our primary business is profile cutting of materials to customers specifications using high-pressure water with abrasive.
We are looking for creative ideas and are open to suggestions!
http://brightfordcutworks.com/index.asp?pid=1
Update:
Cut quality picture (uploaded)
Map
Comparison to other profile cutting methods such as plasma/laser
Single page style without continuous scrolling
"We can cut virtually any material from any drawing whether it be a Full 3D cad models to hand sketched "
Target Market(s)
Film Industry, Prototype, Engineering, Architect, Artisits, one off designs
Industry/Entity Type
Engineering
Number of Pages Required
1 page
Font styles to use
Look and feel

```html
<!DOCTYPE html>
<html lang="en">
<head>
<meta charset="utf-8">
<title>Brightford Cutworks</title>
<link href="https://fonts.googleapis.com/css2?family=Alegreya+Sans:wght@300;400;500;700&family=Arimo:wght@400;700&display=swap" rel="stylesheet">
<style>
:root{
  --blue:#2f6fb5;
  --blue-dark:#245a97;
  --blue-pale:#c9dcf0;
  --ink:#3d3d3d;
  --muted:#555;
  --grey-bg:#eeeeee;
  --white:#ffffff;
  --head:"Alegreya Sans",sans-serif;
  --body:"Arimo",sans-serif;
}
*{margin:0;padding:0;box-sizing:border-box}
html,body{width:1200px;height:3622px;overflow:hidden;background:var(--white)}
body{position:relative;font-family:var(--body);color:var(--muted)}
section,header,footer{position:absolute;left:0;width:1200px}
.abs{position:absolute}
.btn{position:absolute;display:flex;align-items:center;justify-content:center;background:var(--blue);color:var(--white);font-family:var(--head);font-size:18px;text-transform:uppercase;border-radius:26px;letter-spacing:.5px}

/* header */
.site-header{top:0;height:116px;background:var(--white)}
.brand{left:84px;top:30px;display:flex;align-items:center;gap:14px}
.brand-mark{width:22px;height:22px;border-radius:50%;background:var(--blue)}
.brand-name{font-family:var(--head);font-weight:700;font-size:38px;color:var(--blue-dark);letter-spacing:1px}
.nav{left:582px;top:0;height:116px;display:flex}
.nav a{display:flex;align-items:center;justify-content:center;height:116px;font-family:var(--head);font-size:19px;color:var(--ink);text-decoration:none;padding:0 28px}
.nav a.active{background:var(--blue);color:var(--white);width:108px;padding:0}
.search{left:1078px;top:34px;width:48px;height:48px;border-radius:50%;background:var(--white);box-shadow:0 0 8px rgba(0,0,0,.18);display:flex;align-items:center;justify-content:center}

/* hero */
.hero{top:116px;height:572px;background:linear-gradient(135deg,#8a98a8,#5f6f80 45%,#3e4b58)}
.hero-title{top:170px;width:1200px;text-align:center;font-family:var(--head);font-weight:700;color:var(--white);font-size:62px;letter-spacing:1px}
.hero-title small{font-size:48px}
.hero-sub{top:258px;left:300px;width:600px;text-align:center;color:var(--white);font-size:18px;line-height:29px}
.hero .btn{left:529px;top:350px;width:142px;height:46px;font-size:17px}
.dots{left:548px;top:509px;display:flex;gap:18px;align-items:center}
.dots span{width:20px;height:20px;border-radius:50%;background:rgba(255,255,255,.55)}
.dots span.on{background:var(--white)}

/* welcome */
.welcome{top:688px;height:548px}
.photo{position:absolute}
.welcome .photo{left:126px;top:63px;width:480px;height:422px;background:linear-gradient(160deg,#7d8590,#b9a6b0 55%,#d8c4cc)}
.kicker{font-family:var(--head);font-weight:300;font-size:40px;color:var(--ink);line-height:44px}
.headline{font-family:var(--head);font-weight:400;font-size:40px;color:var(--blue);line-height:46px;text-transform:uppercase}
.lead{color:var(--blue);font-size:18px;line-height:30px}
.copy{font-size:14.5px;line-height:27px;color:var(--muted)}
.welcome .kicker{left:652px;top:62px}
.welcome .headline{left:652px;top:112px}
.welcome .lead{left:652px;top:170px;width:430px}
.welcome .copy{left:652px;top:250px;width:430px}
.welcome .btn{left:650px;top:435px;width:135px;height:50px}

/* gallery */
.gallery{top:1236px;height:719px;background:var(--grey-bg)}
.sec-title{width:1200px;text-align:center;font-family:var(--head);font-size:38px;color:var(--ink);font-weight:400}
.sec-title em{font-style:normal;color:var(--blue);text-transform:uppercase}
.gallery .sec-title{top:50px}
.gallery svg{position:absolute;left:0;top:0}

/* materials */
.materials{top:1955px;height:548px}
.materials .headline{left:80px;top:63px;font-size:40px}
.materials .lead{left:80px;top:124px;width:460px}
.materials .copy{left:80px;top:202px;width:470px;white-space:nowrap}
.materials .btn{left:80px;top:435px;width:134px;height:50px}
.materials .photo{left:594px;top:63px;width:480px;height:423px;background:linear-gradient(150deg,#5b6470,#a7b0b9 55%,#6d7680)}

/* news */
.news{top:2503px;height:616px;background:var(--grey-bg)}
.news .sec-title{top:60px}
.news-intro{top:142px;left:250px;width:700px;text-align:center;font-size:15px;line-height:27px}
.card{position:absolute;top:213px;width:323px}
.card-img{height:205px;position:relative}
.card-meta{position:absolute;left:0;bottom:0;width:100%;height:41px;background:rgba(47,111,181,.85);display:flex;align-items:center;gap:20px;padding-left:14px;color:var(--white);font-size:12px}
.card-meta span{display:flex;align-items:center;gap:6px}
.card h3{margin-top:22px;width:290px;font-size:17px;line-height:29px;color:var(--blue);font-weight:400}
.card p{margin-top:6px;width:290px;font-size:14px;line-height:26px}

/* newsletter */
.newsletter{top:3119px;height:302px}
.nl-visual{left:331px;top:19px;width:86px;height:56px;background:var(--blue-pale)}
.newsletter .sec-title{top:64px}
.newsletter .sec-title em{text-transform:none}
.nl-sub{top:142px;width:1200px;text-align:center;font-size:14px}
.field{position:absolute;top:188px;width:321px;height:51px;border-radius:26px;background:var(--white);box-shadow:0 0 12px rgba(0,0,0,.13);font-size:14px;color:#888;display:flex;align-items:center;padding-left:30px}
.newsletter .btn{left:876px;top:188px;width:135px;height:51px}

/* footer */
.site-footer{top:3421px;height:201px;background:var(--blue);color:var(--white)}
.foot-nav{top:40px;width:1200px;display:flex;justify-content:center;gap:26px;font-size:15px}
.socials{top:86px;width:1200px;display:flex;justify-content:center;gap:22px}
.socials span{width:36px;height:36px;border-radius:50%;background:var(--white)}
.rule{left:77px;top:140px;width:1046px;height:1px;background:rgba(255,255,255,.6)}
.copyright{top:160px;width:1200px;text-align:center;font-size:14px}
</style>
</head>
<body>

<header class="site-header">
  <div class="abs brand"><span class="brand-mark"></span><span class="brand-name">BRIGHTFORD CUTWORKS</span></div>
  <nav class="abs nav">
    <a class="active">Home</a><a>About Us</a><a>Materials</a><a>Gallery</a>
  </nav>
  <div class="abs search">
    <svg width="22" height="22" viewBox="0 0 22 22"><circle cx="9" cy="9" r="6.5" fill="none" stroke="#2f6fb5" stroke-width="2.5"/><line x1="14" y1="14" x2="20" y2="20" stroke="#2f6fb5" stroke-width="3" stroke-linecap="round"/></svg>
  </div>
</header>

<section class="hero" role="img" aria-label="Waterjet cutting head working over a metal sheet, blue-grey toned">
  <h1 class="abs hero-title">BRIGHTFORD <small>CUTWORKS</small></h1>
  <p class="abs hero-sub">Lorem Ipsum is simply dummy text of the printing and typesetting industry. Lorem Ipsum has been the industry's standard</p>
  <a class="btn">Contact Us</a>
  <div class="abs dots"><span></span><span class="on"></span><span></span></div>
</section>

<section class="welcome">
  <svg class="abs" width="1200" height="548" viewBox="0 0 1200 548"><polygon points="0,0 398,0 355,470 398,548 0,548" fill="#2f6fb5"/></svg>
  <div class="photo" role="img" aria-label="Waterjet nozzle cutting with water spray"></div>
  <p class="abs kicker">Welcome To</p>
  <h2 class="abs headline">Brightford Cutworks</h2>
  <p class="abs lead">Waterjet cutting offers a soloution where other technologies struggle</p>
  <p class="abs copy">Brightford Cutworks is part of the Meridian Arts Group who have been providing a model making and profile cutting service primarily to the film industry for over 10 years. We are used to working within tight timeframes with a fast turnaround for all aspects of Water Jet Profiling, Tile Water Jet Cutting, Abrasive Steel Cutting and Foam Water Jet Cutting.</p>
  <a class="btn">Learn More</a>
</section>

<section class="gallery">
  <svg width="1200" height="719" viewBox="0 0 1200 719">
    <defs>
      <linearGradient id="gA" x1="0" y1="0" x2="1" y2="1"><stop offset="0" stop-color="#9aa3ad"/><stop offset="1" stop-color="#4d5864"/></linearGradient>
      <linearGradient id="gB" x1="0" y1="0" x2="1" y2="1"><stop offset="0" stop-color="#2c3d36"/><stop offset="1" stop-color="#6a9a86"/></linearGradient>
      <linearGradient id="gC" x1="0" y1="0" x2="1" y2="1"><stop offset="0" stop-color="#3a6fb8"/><stop offset="1" stop-color="#9cc0e6"/></linearGradient>
      <linearGradient id="gD" x1="0" y1="0" x2="1" y2="1"><stop offset="0" stop-color="#6d7680"/><stop offset="1" stop-color="#c2a04a"/></linearGradient>
    </defs>
    <g stroke="#ffffff" stroke-width="6">
      <g role="img" aria-label="Gallery of waterjet cutting photographs">
        <polygon points="205,123 326,244 205,365 84,244" fill="url(#gA)"/>
        <polygon points="471,123 592,244 471,365 350,244" fill="url(#gA)"/>
        <polygon points="736,123 857,244 736,365 615,244" fill="url(#gB)"/>
        <polygon points="995,123 1116,244 995,365 874,244" fill="url(#gC)"/>
        <polygon points="338,268 459,389 338,510 217,389" fill="url(#gB)"/>
        <polygon points="599,268 720,389 599,510 478,389" fill="url(#gC)"/>
        <polygon points="864,268 985,389 864,510 743,389" fill="url(#gD)"/>
        <polygon points="471,405 592,526 471,647 350,526" fill="url(#gB)"/>
        <polygon points="729,405 850,526 729,647 608,526" fill="url(#gC)"/>
      </g>
    </g>
    <g fill="none" stroke="#2f6fb5" stroke-width="1.5">
      <polygon points="205,116 333,244 205,372 77,244"/>
      <polygon points="471,116 599,244 471,372 343,244"/>
      <polygon points="736,116 864,244 736,372 608,244"/>
      <polygon points="995,116 1123,244 995,372 867,244"/>
      <polygon points="338,261 466,389 338,517 210,389"/>
      <polygon points="599,261 727,389 599,517 471,389"/>
      <polygon points="864,261 992,389 864,517 736,389"/>
      <polygon points="471,398 599,526 471,654 343,526"/>
      <polygon points="729,398 857,526 729,654 601,526"/>
    </g>
    <circle cx="597" cy="386" r="11" fill="none" stroke="#fff" stroke-width="3"/>
    <line x1="605" y1="394" x2="614" y2="403" stroke="#fff" stroke-width="3"/>
  </svg>
  <h2 class="abs sec-title">Our <em>Gallery</em></h2>
</section>

<section class="materials">
  <svg class="abs" width="1200" height="548" viewBox="0 0 1200 548"><polygon points="804,0 1200,0 1200,548 804,548 845,470" fill="#2f6fb5"/></svg>
  <h2 class="abs headline">Materials</h2>
  <p class="abs lead">It is possible to cut virtually any profile in any material with waterjet</p>
  <p class="abs copy">Materials we can cut include, but are not limited to, all metals<br>and alloys, stone and ceramics, composites,<br>corian, wood, glass, acrylics, resins, silicones, plastics, foams,<br>carpet and felts. We can also cut laminated<br>dissimilar materials which can often be very hard to cut using<br>conventional methods. We are always happy<br>to test cut a sample of your material free of charge to<br>demonstrate the quality of cut achievable.</p>
  <a class="btn">Learn More</a>
  <div class="photo" role="img" aria-label="Close-up of waterjet cutting head over a machined metal plate"></div>
</section>

<section class="news">
  <h2 class="abs sec-title">Latest <em>News</em></h2>
  <p class="abs news-intro">Lorem Ipsum is simply dummy text of the printing and typesetting industry. Lorem Ipsum has been the industry's standard dummy text ever since the 1500s.</p>
  <article class="card" style="left:77px">
    <div class="card-img" role="img" aria-label="Waterjet machine cutting a grey metal sheet" style="background:linear-gradient(160deg,#c9ced4,#8a939c)">
      <div class="card-meta"><span>&#9638; 23 Oct, 2017</span><span>&#9679; Admin</span><span>&#9633; 18 Comments</span></div>
    </div>
    <h3>Lorem Ipsum is simply dummy<br>the printing typesetting industry.</h3>
    <p>Lorem Ipsum is simply dummy text of the .<br>Lorem Ipsum has been the industry's.</p>
  </article>
  <article class="card" style="left:438px">
    <div class="card-img" role="img" aria-label="Waterjet cutting head under blue light" style="background:linear-gradient(160deg,#2a3f8a,#6d86c8)">
      <div class="card-meta"><span>&#9638; 23 Oct, 2017</span><span>&#9679; Admin</span><span>&#9633; 18 Comments</span></div>
    </div>
    <h3>Lorem Ipsum is simply dummy<br>the printing typesetting industry.</h3>
    <p>Lorem Ipsum is simply dummy text of the .<br>Lorem Ipsum has been the industry's.</p>
  </article>
  <article class="card" style="left:799px">
    <div class="card-img" role="img" aria-label="Cutting head with yellow fitting over wet blue surface" style="background:linear-gradient(160deg,#7fa6d6,#3f6fa8)">
      <div class="card-meta"><span>&#9638; 23 Oct, 2017</span><span>&#9679; Admin</span><span>&#9633;</span></div>
    </div>
    <h3>Lorem Ipsum is simply dummy<br>the printing typesetting industry.</h3>
    <p>Lorem Ipsum is simply dummy text of the .<br>Lorem Ipsum has been the industry's.</p>
  </article>
</section>

<section class="newsletter">
  <div class="abs nl-visual" role="img" aria-label="Small decorative graphic for the newsletter"></div>
  <h2 class="abs sec-title">News<em>letter</em></h2>
  <p class="abs nl-sub">For latest news and updates subscribe our newsletter</p>
  <div class="field" style="left:210px">Enter Name*</div>
  <div class="field" style="left:541px">Enter E-mail*</div>
  <a class="btn">Subscribe</a>
</section>

<footer class="site-footer">
  <nav class="abs foot-nav"><span>Home</span><span>|</span><span>About Us</span><span>|</span><span>Materials</span><span>|</span><span>Gallery</span></nav>
  <div class="abs socials"><span></span><span></span><span></span></div>
  <div class="abs rule"></div>
  <p class="abs copyright">&copy; BRIGHTFORD CUTWORKS - 2018. All Rights Reserved.</p>
</footer>

</body>
</html>
```